Recycling Depot Business Card Design

We need a double sided business card for our recycling depot business. Please include name, position, address, phone, cell, fax, email and website address. Business card should match the colour scheme of our logo and look environmental but modern. I've attached a few business cards from Sketch Harbor that I like.

Industry/Entity Type

Recycling

Contact Information for Business Card

Please include name, position, address, phone, cell, fax, email and website address.

Font styles to use
Sans Serif

Requirements
Must have
• Our Logo, Colour Scheme that matches our logo. Use of Colour Gradients and a custom look.

```html
<!DOCTYPE html>
<html lang="en">
<head>
<meta charset="utf-8">
<title>Loopward Business Card</title>
<link rel="stylesheet" href="https://fonts.googleapis.com/css2?family=Montserrat:wght@300;400;500;800&family=Open+Sans:wght@400;700&display=swap">
<style>
  :root {
    --page: #e9ecea;
    --card: #ffffff;
    --green-lime: #8cc63f;
    --green-mid: #3f9a3a;
    --green-deep: #17683a;
    --ink: #111111;
    --grey-text: #555b57;
    --pattern-light: #f4f5f4;
    --pattern-grey: #e2e4e2;
  }
  * { box-sizing: border-box; margin: 0; padding: 0; }
  html, body { width: 1200px; height: 900px; overflow: hidden; }
  body {
    background: var(--page);
    display: flex;
    flex-direction: column;
    align-items: center;
    justify-content: center;
    gap: 60px;
    font-family: "Montserrat", sans-serif;
  }
  .card {
    position: relative;
    width: 600px;
    height: 343px;
    border-radius: 22px;
    background: var(--card);
    overflow: hidden;
    box-shadow: 0 6px 18px rgba(0,0,0,0.12);
  }

  /* Front */
  .front-brand {
    position: absolute;
    left: 56px;
    top: 62px;
    display: flex;
    align-items: center;
    gap: 12px;
  }
  .brand-dot {
    width: 34px; height: 34px;
    border-radius: 50%;
    background: var(--green-mid);
  }
  .brand-name {
    font-family: "Open Sans", sans-serif;
    font-weight: 700;
    font-size: 32px;
    color: var(--green-deep);
    letter-spacing: -0.5px;
  }
  .person {
    position: absolute;
    left: 330px;
    top: 92px;
  }
  .person-name {
    font-weight: 800;
    font-size: 25px;
    letter-spacing: 1px;
    color: var(--ink);
  }
  .person-title {
    font-weight: 300;
    font-size: 19px;
    color: var(--ink);
    margin-top: 2px;
  }
  .contact-band {
    position: absolute;
    left: 0; right: 0; bottom: 0;
    height: 132px;
    background: linear-gradient(100deg, var(--green-lime) 0%, var(--green-mid) 30%, var(--green-deep) 62%, var(--green-mid) 85%, var(--green-lime) 100%);
    display: flex;
    justify-content: space-between;
    padding: 34px 48px 0 44px;
  }
  .contact-group { list-style: none; }
  .contact-item {
    display: flex;
    align-items: flex-start;
    gap: 10px;
    color: #ffffff;
    font-size: 11.5px;
    font-weight: 400;
    letter-spacing: 0.6px;
    line-height: 1.45;
    margin-bottom: 8px;
  }
  .contact-icon {
    flex: none;
    width: 17px; height: 17px;
    border-radius: 50%;
    background: var(--green-lime);
    display: flex; align-items: center; justify-content: center;
    margin-top: 1px;
  }
  .contact-icon svg { width: 10px; height: 10px; }

  /* Back */
  .back-field {
    position: absolute;
    inset: 0;
    background: radial-gradient(circle at 50% 50%, var(--pattern-light) 0%, var(--pattern-grey) 100%);
  }
  .back-mark {
    position: absolute;
    left: 50%; top: 50%;
    transform: translate(-50%, -50%);
    text-align: center;
  }
  .back-brand {
    font-family: "Open Sans", sans-serif;
    font-weight: 700;
    font-size: 60px;
    color: var(--green-deep);
    letter-spacing: -1px;
    line-height: 1;
  }
  .back-tagline {
    font-family: "Open Sans", sans-serif;
    font-weight: 400;
    font-size: 19px;
    color: var(--grey-text);
    letter-spacing: 1px;
    margin-top: 10px;
    word-spacing: 26px;
  }
</style>
</head>
<body>

  <section class="card card-front">
    <div class="front-brand">
      <span class="brand-dot"></span>
      <span class="brand-name">Loopward</span>
    </div>

    <div class="person">
      <p class="person-name">JANATHAN DOE</p>
      <p class="person-title">Job Tittle Here</p>
    </div>

    <div class="contact-band">
      <ul class="contact-group">
        <li class="contact-item">
          <span class="contact-icon">
            <svg viewBox="0 0 10 10"><path d="M5 0.8a3 3 0 0 0-3 3c0 2.2 3 5.4 3 5.4s3-3.2 3-5.4a3 3 0 0 0-3-3z" fill="#fff"/><circle cx="5" cy="3.8" r="1.1" fill="#8cc63f"/></svg>
          </span>
          <span>CITY ADDRESS STREET<br>HOME LOCATION GOES HERE</span>
        </li>
        <li class="contact-item">
          <span class="contact-icon">
            <svg viewBox="0 0 10 10"><rect x="1" y="2.5" width="8" height="5.5" fill="#fff"/><path d="M1 2.5l4 3.2 4-3.2" fill="none" stroke="#8cc63f" stroke-width="0.9"/></svg>
          </span>
          <span>BRAND-NAME@EMAIL.COM</span>
        </li>
      </ul>
      <ul class="contact-group">
        <li class="contact-item">
          <span class="contact-icon">
            <svg viewBox="0 0 10 10"><path d="M2.6 1.2l1.4 1.9-0.8 1c0.5 1 1.2 1.7 2.2 2.2l1-0.8 1.9 1.4-0.7 1.5c-3.6-0.3-6.1-2.8-6.4-6.4z" fill="#fff"/></svg>
          </span>
          <span>+000 1234 5678 999<br>+012 9934 5271 003</span>
        </li>
        <li class="contact-item">
          <span class="contact-icon">
            <svg viewBox="0 0 10 10" fill="none" stroke="#fff" stroke-width="0.9"><circle cx="5" cy="5" r="3.8"/><ellipse cx="5" cy="5" rx="1.6" ry="3.8"/><path d="M1.2 5h7.6"/></svg>
          </span>
          <span>WWW.BRANDNAME.COM</span>
        </li>
      </ul>
    </div>
  </section>

  <section class="card card-back">
    <div class="back-field" role="img" aria-label="Repeating light grey pattern of the recycling emblem across the card"></div>
    <div class="back-mark">
      <p class="back-brand">Loopward</p>
      <p class="back-tagline">Resource Recovery</p>
    </div>
  </section>

</body>
</html>
```